IT Company looking to market towards Dental Offices

I am looking for a full-color design. Using my existing logo. Must have High Res stock photos. The brochure needs to be full page edge to edge design single fold pamphlet style. Content provided. Please see the website in attached Word Doc for more content.

```html
<!DOCTYPE html>
<html lang="en">
<head>
<meta charset="utf-8">
<title>Byte Harbor – Dental IT Brochure</title>
<link href="https://fonts.googleapis.com/css2?family=Open+Sans:ital,wght@0,400;0,600;0,700;0,800;1,600&display=swap" rel="stylesheet">
<style>
:root{
  --bg:#eceef0;
  --navy:#13306d;
  --navy-deep:#0c2253;
  --blue:#1f5fb8;
  --sky:#3d8fd9;
  --ink:#1b2d5c;
  --text:#3a4250;
  --paper:#ffffff;
  --mist:#e6e9ee;
  --photo-a:#c9d3df;
  --photo-b:#6f88ad;
}
*{margin:0;padding:0;box-sizing:border-box}
html,body{width:1200px;height:2575px;overflow:hidden;background:var(--bg)}
body{font-family:"Open Sans",Arial,sans-serif;color:var(--text);position:relative}
.sheet{position:absolute;display:flex;box-shadow:0 6px 22px rgba(20,30,60,.18)}
.sheet--cover{left:330px;top:120px}
.sheet--outside{left:60px;top:938px}
.sheet--inside{left:60px;top:1756px}
.page{position:relative;width:540px;height:699px;background:var(--paper);overflow:hidden}
.layer{position:absolute;left:0;top:0;display:block}
.brand{position:absolute;display:flex;align-items:center;gap:10px;font-weight:700;white-space:nowrap}
.brand__dot{width:30px;height:30px;border-radius:50%;background:currentColor}
.brand--light{color:#fff;font-size:26px}
.brand--dark{color:var(--navy);font-size:26px}
.phone-pill{position:absolute;left:70px;top:548px;width:400px;height:36px;border-radius:18px;background:var(--blue);color:#fff;font-weight:700;font-size:21px;display:flex;align-items:center;justify-content:center;gap:10px;letter-spacing:.5px}
.icon{width:18px;height:18px;flex:none}
.tagline{position:absolute;left:20px;right:20px;top:596px;text-align:center;color:var(--ink);font-weight:800;font-size:15.5px;line-height:1.3;text-transform:uppercase}
.body-copy{position:absolute;font-size:11.5px;line-height:1.5;color:var(--text)}
.body-copy p{margin-bottom:9px}
.body-copy strong{color:var(--ink)}
.contact{position:absolute;left:28px;top:590px;color:#fff;font-size:13px;line-height:1.9;list-style:none}
.contact li{display:flex;align-items:center;gap:10px}
.about{position:absolute;left:30px;top:24px;right:40px;color:#fff}
.about__head{display:flex;align-items:center;gap:14px;font-weight:700;font-size:14px;margin-bottom:10px}
.about__head .brand{position:static;font-size:16px}
.about__head .brand__dot{width:18px;height:18px}
.about p{font-size:10.5px;line-height:1.45;margin-bottom:7px;color:#dfe7f5}
.service{position:absolute;left:30px;display:flex;gap:14px}
.service__icon{width:40px;height:40px;border-radius:50%;background:var(--blue);border:3px solid #cfe0f5;flex:none}
.service h3{font-size:11px;font-weight:800;color:var(--ink);text-transform:uppercase;margin-bottom:2px}
.service__cols{display:flex;gap:26px}
.service ul{list-style:none;font-size:9.5px;line-height:1.45;color:var(--text)}
.service ul li::before{content:"– "}
.cta-title{position:absolute;left:40px;right:40px;top:300px;height:32px;background:var(--blue);color:#fff;font-weight:800;font-size:14px;display:flex;align-items:center;justify-content:center;text-transform:uppercase}
.steps{position:absolute;left:40px;right:40px;top:332px;border:1.5px solid var(--sky);background:#fff;padding:10px 16px 12px}
.steps h4{text-align:center;font-size:12px;font-weight:600;color:var(--ink);margin-bottom:8px}
.steps ol{list-style:none;font-size:11.5px;line-height:1.55;color:var(--text)}
.steps li{display:flex;gap:8px;border-top:1px solid var(--mist);padding:2px 0}
.steps li span{color:var(--blue);font-weight:800}
.cta-copy{position:absolute;left:60px;right:60px;top:474px;text-align:center;font-size:11.5px;line-height:1.5;color:var(--text)}
.cta-copy p{margin-bottom:10px}
.call-now{position:absolute;right:30px;bottom:26px;color:#fff;font-weight:800;font-size:18px;display:flex;align-items:center;gap:10px;letter-spacing:.5px}
</style>
</head>
<body>

<svg width="0" height="0" style="position:absolute" aria-hidden="true">
  <defs>
    <linearGradient id="navyFill" x1="0" y1="0" x2="1" y2="1">
      <stop offset="0" stop-color="#1a3f8a"/><stop offset="1" stop-color="#0c2253"/>
    </linearGradient>
    <linearGradient id="roomPhoto" x1="0" y1="0" x2="1" y2="1">
      <stop offset="0" stop-color="#dfe5ec"/><stop offset=".55" stop-color="#a9b8ca"/><stop offset="1" stop-color="#5f7aa3"/>
    </linearGradient>
    <linearGradient id="mistFill" x1="0" y1="0" x2="0" y2="1">
      <stop offset="0" stop-color="#ffffff"/><stop offset="1" stop-color="#d9dee6"/>
    </linearGradient>
    <symbol id="phone" viewBox="0 0 24 24"><circle cx="12" cy="12" r="11" fill="none" stroke="currentColor" stroke-width="2"/><path d="M8.5 6.5l2 2-1.2 1.6c.8 1.8 2 3 3.6 3.8l1.6-1.2 2 2-1.4 1.8c-4-.6-7.6-4.2-8.2-8.2z" fill="currentColor"/></symbol>
    <symbol id="globe" viewBox="0 0 24 24"><circle cx="12" cy="12" r="10" fill="none" stroke="currentColor" stroke-width="2"/><path d="M2 12h20M12 2c3 3 3 17 0 20M12 2c-3 3-3 17 0 20" fill="none" stroke="currentColor" stroke-width="1.6"/></symbol>
    <symbol id="pin" viewBox="0 0 24 24"><path d="M12 2a7 7 0 0 1 7 7c0 5-7 13-7 13S5 14 5 9a7 7 0 0 1 7-7z" fill="currentColor"/><circle cx="12" cy="9" r="2.6" fill="#1f5fb8"/></symbol>
  </defs>
</svg>

<!-- Front cover -->
<section class="sheet sheet--cover">
  <article class="page page--front">
    <svg class="layer" width="540" height="699" role="img" aria-label="Photo of a modern dental treatment room with blue patient chairs and overhead lights">
      <path d="M0 200 Q270 90 540 70 V530 H0 Z" fill="url(#roomPhoto)"/>
    </svg>
    <svg class="layer" width="540" height="699" aria-hidden="true">
      <path d="M0 0 H540 V55 Q280 80 0 195 Z" fill="url(#navyFill)"/>
      <path d="M0 204 Q270 92 540 66" fill="none" stroke="#3d8fd9" stroke-width="7"/>
      <path d="M0 530 H540 V699 H0 Z" fill="url(#mistFill)"/>
      <path d="M0 520 Q270 545 540 505 V540 Q270 570 0 548 Z" fill="#e9edf3"/>
      <path d="M0 672 Q300 640 540 600 V699 H0 Z" fill="#1f5fb8"/>
      <path d="M0 664 Q300 630 540 590" fill="none" stroke="#9fc3ea" stroke-width="3"/>
    </svg>
    <div class="brand brand--light" style="left:44px;top:46px"><span class="brand__dot"></span>Byte Harbor</div>
    <div class="phone-pill"><svg class="icon"><use href="#phone"/></svg>555-014-2287</div>
    <p class="tagline">Offsite backups for your practice management software<br>made easy and automated</p>
  </article>
</section>

<!-- Outside spread: back + front -->
<section class="sheet sheet--outside">
  <article class="page page--back">
    <svg class="layer" width="540" height="699" role="img" aria-label="Photo of a dentist and assistant treating a patient in a bright clinic">
      <path d="M0 0 H540 V250 Q270 285 0 262 Z" fill="url(#roomPhoto)"/>
    </svg>
    <svg class="layer" width="540" height="699" aria-hidden="true">
      <path d="M0 440 Q120 560 540 610 V699 H0 Z" fill="url(#navyFill)"/>
      <path d="M0 425 Q120 548 540 598" fill="none" stroke="#3d8fd9" stroke-width="6"/>
    </svg>
    <div class="body-copy" style="left:40px;top:290px;width:440px">
      <p>Offsite backups for your practice management software made easy and automated. We know how important your Dental software is, and we securely back up every night to an encrypted, off-site location so your data is always protected.</p>
      <p><strong>Get started today at www.dentalvaultbackup.com</strong></p>
      <p>We don't charge anything until we have confirmed that your data has been successfully saved to our encrypted servers.</p>
    </div>
    <div class="brand brand--dark" style="left:270px;top:500px"><span class="brand__dot"></span>Byte Harbor</div>
    <ul class="contact">
      <li><svg class="icon"><use href="#phone"/></svg>555-014-2287</li>
      <li><svg class="icon"><use href="#globe"/></svg>www.byteharborit.com</li>
      <li><svg class="icon"><use href="#pin"/></svg>480 Maple Crest Ave, Lakeview, MO 65000</li>
    </ul>
  </article>
  <article class="page page--front">
    <svg class="layer" width="540" height="699" role="img" aria-label="Photo of a modern dental treatment room with blue patient chairs and overhead lights">
      <path d="M0 200 Q270 90 540 70 V530 H0 Z" fill="url(#roomPhoto)"/>
    </svg>
    <svg class="layer" width="540" height="699" aria-hidden="true">
      <path d="M0 0 H540 V55 Q280 80 0 195 Z" fill="url(#navyFill)"/>
      <path d="M0 204 Q270 92 540 66" fill="none" stroke="#3d8fd9" stroke-width="7"/>
      <path d="M0 530 H540 V699 H0 Z" fill="url(#mistFill)"/>
      <path d="M0 520 Q270 545 540 505 V540 Q270 570 0 548 Z" fill="#e9edf3"/>
      <path d="M0 672 Q300 640 540 600 V699 H0 Z" fill="#1f5fb8"/>
      <path d="M0 664 Q300 630 540 590" fill="none" stroke="#9fc3ea" stroke-width="3"/>
    </svg>
    <div class="brand brand--light" style="left:44px;top:46px"><span class="brand__dot"></span>Byte Harbor</div>
    <div class="phone-pill"><svg class="icon"><use href="#phone"/></svg>555-014-2287</div>
    <p class="tagline">Offsite backups for your practice management software<br>made easy and automated</p>
  </article>
</section>

<!-- Inside spread -->
<section class="sheet sheet--inside">
  <article class="page page--about">
    <svg class="layer" width="540" height="699" aria-hidden="true">
      <path d="M0 0 H540 V190 Q300 210 0 300 Z" fill="url(#navyFill)"/>
      <path d="M0 312 Q300 220 540 200" fill="none" stroke="#3d8fd9" stroke-width="5"/>
      <path d="M0 660 Q270 640 540 650 V699 H0 Z" fill="#1f5fb8"/>
    </svg>
    <div class="about">
      <div class="about__head"><span class="brand"><span class="brand__dot"></span>Byte Harbor</span>ABOUT US</div>
      <p>Byte Harbor offers a proven expertise in Dental Practices. We have trained engineers that specialize in dental practice management solutions. We can handle everything from hardware to software and keep your office running smoothly every day.</p>
      <p>Being familiar with Dental technology and how your practice runs, we are able to provide you with the right solutions and support. We partner with the best vendors so your practice gets the care it deserves.</p>
    </div>
    <div class="service" style="top:318px">
      <span class="service__icon"></span>
      <div><h3>Hardware Sales</h3>
        <div class="service__cols">
          <ul><li>Servers</li><li>Workstations</li><li>Firewalls</li><li>Routers</li></ul>
          <ul><li>Switches</li><li>TVs &amp; Monitors</li><li>Wireless Equipment</li><li>Custom Check-In Workstations</li></ul>
        </div></div>
    </div>
    <div class="service" style="top:410px">
      <span class="service__icon"></span>
      <div><h3>Infrastructure</h3>
        <div class="service__cols">
          <ul><li>Data &amp; Voice Cable</li><li>HDMI &amp; VGA Video Cable</li><li>TV &amp; Dual Monitor Installation</li><li>Mounting Hardware</li></ul>
          <ul><li>Wireless Installation</li><li>Office Layout Solutions</li><li>Custom Owned Cable</li><li>Video Surveillance</li></ul>
        </div></div>
    </div>
    <div class="service" style="top:502px">
      <span class="service__icon"></span>
      <div><h3>Solutions</h3>
        <ul><li>Flat Rate Monthly Support</li><li>Secure Email with Encryption</li><li>Secure Backups Onsite &amp; Offsite</li><li>Practice Management Software Support</li><li>Patient Communication Solutions</li><li>HIPAA Compliance and Cyber Security</li><li>Data Backup Solutions</li></ul>
      </div>
    </div>
    <svg class="layer" style="left:370px;top:520px" width="140" height="120" role="img" aria-label="Photo of a desktop computer with monitor, keyboard and tower">
      <rect x="0" y="0" width="140" height="120" rx="6" fill="#3a3f48"/>
    </svg>
  </article>
  <article class="page page--cta">
    <svg class="layer" width="540" height="699" role="img" aria-label="Photo of a clean dental operatory with chair and monitor">
      <path d="M0 0 H540 V250 Q300 275 0 260 Z" fill="url(#roomPhoto)"/>
    </svg>
    <svg class="layer" width="540" height="699" aria-hidden="true">
      <path d="M0 699 Q260 640 540 590 V699 Z" fill="url(#navyFill)"/>
      <path d="M0 690 Q260 628 540 576" fill="none" stroke="#3d8fd9" stroke-width="5"/>
    </svg>
    <h2 class="cta-title">Ready to make your technology work?</h2>
    <div class="steps">
      <h4>How To Achieve Technology Bliss For Your Practice:</h4>
      <ol>
        <li><span>1</span>Schedule a FREE Network &amp; Technology Evaluation</li>
        <li><span>2</span>Receive your Flat Rate Price and Technology Guide</li>
        <li><span>3</span>Sit back and let Byte Harbor take care of everything</li>
      </ol>
    </div>
    <div class="cta-copy">
      <p>Don't let Technology Departments, Hardware Vendors and Practice Management vendors point fingers at each other.</p>
      <p>We collaborate everything and everyone for you, make one call to us and let us handle your technology.</p>
    </div>
    <div class="call-now">CALL US NOW! <svg class="icon"><use href="#phone"/></svg>555-014-2287</div>
  </article>
</section>

</body>
</html>
```